Venture firm needs flyer to attract Sales Professionals as Advisors

Creation of either a pdf Flyer or Brochure.
The target audience are senior sales professionals of the Information Technology industry. The flyer needs to come across highly professional, business oriented, positive. Text for the brochure is attached. The colors/graphics should align with Tormid Ventures corporate appearance: www.tormid-example.ventures

Target Market(s)

Sales Professionals in the Information Technology Industry

Industry/Entity Type

Information Technology

Font styles to use
Other font styles liked:
• Raleway

Requirements
Must have
• fitting the corporate look and feel: www.tormid-example.ventures

```html
<!DOCTYPE html>
<html lang="en">
<head>
<meta charset="utf-8">
<title>Tormid Sales Council Flyer</title>
<link href="https://fonts.googleapis.com/css2?family=Raleway:wght@400;500;600;700;800&family=Lato:wght@400;700&family=Roboto+Condensed:wght@700&display=swap" rel="stylesheet">
<style>
:root{
  --navy:#123a63;
  --navy-text:#1d3f66;
  --ink:#2b2b2b;
  --grey-line:#c9ccd0;
  --paper:#ffffff;
  --backdrop:#ffffff;
}
*{margin:0;padding:0;box-sizing:border-box}
html,body{width:1200px;height:912px;overflow:hidden;background:var(--backdrop)}
.canvas{position:relative;width:1200px;height:912px}
.page{position:absolute;top:79px;width:532px;height:745px;background:var(--paper);overflow:hidden;box-shadow:0 2px 8px rgba(0,0,0,.25)}
.page--front{left:45px}
.page--back{left:623px}
.photo{position:absolute;left:0;top:0;width:532px}
.photo--climber{height:284px;background:linear-gradient(160deg,#5d6b8e 0%,#c9d0de 35%,#f2f4f8 55%,#8c97b3 80%,#4d5a7a 100%)}
.photo--summit{height:334px;background:linear-gradient(180deg,#ffffff 0%,#eef0f2 40%,#c7ccd2 62%,#8d8f8f 78%,#6b5846 100%)}
.brand-tab{position:absolute;right:0;top:0;width:220px;height:69px}
.brand{font-family:'Raleway',sans-serif;font-weight:500;color:var(--navy-text);position:absolute;letter-spacing:.2px}
.brand--tab{right:24px;top:27px;font-size:15px}
.brand--sky{right:16px;top:37px;font-size:21px}
.title{position:absolute;left:0;width:532px;top:307px;text-align:center;font-family:'Raleway',sans-serif;font-weight:800;font-size:28px;color:var(--navy-text);letter-spacing:.3px}
.intro{position:absolute;top:352px;left:19px;width:496px;display:flex;gap:17px;font-family:'Lato',sans-serif;font-size:10.6px;line-height:13.2px;color:var(--ink)}
.intro p{flex:1;text-align:justify;hyphens:auto}
.subhead{position:absolute;left:19px;font-family:'Raleway',sans-serif;font-weight:700;font-size:15px;color:var(--navy-text)}
.band{position:absolute;left:0;width:532px;background:var(--navy);color:#fff;font-family:'Lato',sans-serif;font-size:10.6px;line-height:13.2px;padding:0 19px}
.band p+p{margin-top:13px}
.body-text{position:absolute;left:22px;width:490px;font-family:'Lato',sans-serif;font-size:10.6px;line-height:13.2px;color:var(--ink)}
.phones{position:absolute;left:18px;font-family:'Roboto Condensed',sans-serif;font-weight:700;font-size:21px;color:#4a4d52}
.phones li{list-style:none;display:flex;align-items:baseline;gap:5px;height:29px}
.phones svg{width:11px;height:11px;fill:var(--navy);align-self:center}
.phones .region{font-family:'Raleway',sans-serif;font-weight:600;font-size:14px;color:var(--navy-text)}
.divider{position:absolute;width:1px;height:110px;background:linear-gradient(180deg,rgba(0,0,0,0),#d0d2d5 30%,#d0d2d5 70%,rgba(0,0,0,0))}
.office{position:absolute;width:105px;font-family:'Lato',sans-serif;font-size:9.4px;line-height:13.4px;color:var(--ink)}
.office h3{font-family:'Raleway',sans-serif;font-weight:700;font-size:9.6px;color:var(--navy-text);display:flex;align-items:center;gap:4px;margin-bottom:3px;margin-left:-8px}
.office h3::after{content:"";flex:1;height:4px;background:var(--grey-line)}
.footer-bar{position:absolute;left:0;bottom:0;width:532px;height:22px;background:var(--navy)}
</style>
</head>
<body>
<div class="canvas">

  <section class="page page--front">
    <div class="photo photo--climber" role="img" aria-label="Mountaineer in a yellow jacket standing on a snowy summit ridge above frozen valleys"></div>
    <svg class="brand-tab" viewBox="0 0 220 69"><polygon points="0,0 220,0 220,69 33,69" fill="#fff"/></svg>
    <div class="brand brand--tab">TORMID VENTURES</div>

    <h1 class="title">TORMID SALES COUNCIL (TSC)</h1>
    <div class="intro">
      <p>The TSC is a by invitation only global community of high caliber Sales Professionals in the IT industry. Participating in the TSC provides significant wealth creation opportunities by earning consulting fees and sales commission or finding an exciting startup to work for. TSC members actively collaborate with each</p>
      <p>other to close deals, generate leads &amp; opportunities, navigate through client organizations and build a true advisory status with customers. TSC members get early first hand visibility into the latest technology innovations and learn how those technologies could assist their clients in solving their complex business objectives.</p>
    </div>

    <h2 class="subhead" style="top:466px">How it works:</h2>
    <div class="band" style="top:491px;height:104px;padding-top:18px">
      <p>TSC members will be introduced to Tormid Ventures' client and portfolio companies. This unique ability to learn about latest technology innovation keeps the participants up to date with industry trends and could open interesting earning or employment opportunities. Once exposed to a specific vendor, TSC members can decide if and how they would like to get further involved. Dependent on the interest level for the specific technology, the ability to offer a solution to a known customer problem or the sheer inter-</p>
    </div>

    <ul class="phones" style="top:636px">
      <li><svg viewBox="0 0 24 24"><path d="M6.6 10.8a15 15 0 0 0 6.6 6.6l2.2-2.2c.3-.3.7-.4 1-.2 1.1.4 2.3.6 3.6.6.6 0 1 .4 1 1V20c0 .6-.4 1-1 1A17 17 0 0 1 3 4c0-.6.4-1 1-1h3.5c.6 0 1 .4 1 1 0 1.3.2 2.5.6 3.6.1.3 0 .7-.2 1z"/></svg>+1-650-555 0142 <span class="region">(USA)</span></li>
      <li><svg viewBox="0 0 24 24"><path d="M6.6 10.8a15 15 0 0 0 6.6 6.6l2.2-2.2c.3-.3.7-.4 1-.2 1.1.4 2.3.6 3.6.6.6 0 1 .4 1 1V20c0 .6-.4 1-1 1A17 17 0 0 1 3 4c0-.6.4-1 1-1h3.5c.6 0 1 .4 1 1 0 1.3.2 2.5.6 3.6.1.3 0 .7-.2 1z"/></svg>+49 170 5550188 <span class="region">(Europe)</span></li>
    </ul>
    <div class="divider" style="left:262px;top:618px"></div>
    <div class="office" style="left:286px;top:628px">
      <h3>USA</h3>
      48 Orchard Ave.<br>Palo Alto, CA 94301<br>+1-650-555 0142<br>info@tormid-example.ventures
    </div>
    <div class="office" style="left:412px;top:628px;width:116px">
      <h3>Europe</h3>
      Lindenweg 7<br>10117 Berlin - Germany<br>+49 170 5550188<br>info@tormid-example.ventures
    </div>
    <div class="footer-bar"></div>
  </section>

  <section class="page page--back">
    <div class="photo photo--summit" role="img" aria-label="One climber on a boulder reaching down to pull up a second climber, with cloudy snow-capped mountains behind"></div>
    <div class="brand brand--sky">TORMID VENTURES</div>

    <h2 class="subhead" style="top:349px">As Associates:</h2>
    <p class="body-text" style="top:375px">Associates are actively selling and promoting one or more Tormid Ventures´ portfolio companies. This could be an employment or a freelance opportunity</p>

    <h2 class="subhead" style="top:424px">As Advisors:</h2>
    <div class="band" style="top:447px;height:128px;padding-top:15px">
      <p>Advisors offer their contacts and knowledge about customers to Associates.<br>Advisors could create leads, support with introductions, explain customer organization and processes etc. They will be compensated by Associates with a pre-negotiated % of commission of a future sale that was supported by the Advisor.</p>
      <p>Whatever level of involvement a TSC member seeks there is plenty of opportunity to be rewarded for working with fellow Sales Professionals and Great Startups on the forefront of technical innovation.</p>
    </div>

    <ul class="phones" style="top:622px">
      <li><svg viewBox="0 0 24 24"><path d="M6.6 10.8a15 15 0 0 0 6.6 6.6l2.2-2.2c.3-.3.7-.4 1-.2 1.1.4 2.3.6 3.6.6.6 0 1 .4 1 1V20c0 .6-.4 1-1 1A17 17 0 0 1 3 4c0-.6.4-1 1-1h3.5c.6 0 1 .4 1 1 0 1.3.2 2.5.6 3.6.1.3 0 .7-.2 1z"/></svg>+1-650-555 0142 <span class="region">(USA)</span></li>
      <li><svg viewBox="0 0 24 24"><path d="M6.6 10.8a15 15 0 0 0 6.6 6.6l2.2-2.2c.3-.3.7-.4 1-.2 1.1.4 2.3.6 3.6.6.6 0 1 .4 1 1V20c0 .6-.4 1-1 1A17 17 0 0 1 3 4c0-.6.4-1 1-1h3.5c.6 0 1 .4 1 1 0 1.3.2 2.5.6 3.6.1.3 0 .7-.2 1z"/></svg>+49 170 5550188 <span class="region">(Europe)</span></li>
    </ul>
    <div class="divider" style="left:261px;top:604px"></div>
    <div class="office" style="left:285px;top:614px">
      <h3>USA</h3>
      48 Orchard Ave.<br>Palo Alto, CA 94301<br>+1-650-555 0142<br>info@tormid-example.ventures
    </div>
    <div class="office" style="left:411px;top:614px;width:116px">
      <h3>Europe</h3>
      Lindenweg 7<br>10117 Berlin - Germany<br>+49 170 5550188<br>info@tormid-example.ventures
    </div>
    <div class="footer-bar"></div>
  </section>

</div>
</body>
</html>
```